Pull Up Banner - Recruitment Company

We would like a design for a pull up banner.

For context: we are a recruitment business. We specialise in helping people in healthcare industry to find jobs in Australia.

I have come up with several ideas and text for the banner. Feel free to use the following as you see appropriate:

- Our logo (see attached)
- 'Healthcare Recruitment Agency'
- Some sort of imagine / cartoon of medical professionals (ie. doctor, nurse, physiotherapist, speech pathologist). A cartoon is more friendly than committing to a photo
- 'Empowering your next career move'
- 'Discover tailored opportunities based on your career preferences'
- Dot points (allied health, nursing, medical imaging)
- Contact info at the bottom including our website (www.quellstaffing.com.au, our Instagram handle @quellstaffing, Mobile: XXXX XXX XXX. The title section for contact information could be 'Get in touch:'

Feel free to submit a couple of designs and we can merge aspects that look good on your designs and find the perfect fit.
Thank you
Updates

Hello,

Thank you for your initial submissions to this project. I appreciate the time you've invested.

After reviewing the first attempt, I'd like to share some feedback and initial observations:

- Professionalism and engagement: Is the overall appearance of the banner professional? It's crucial that we have a high-quality design as this will represent our business.

- Image selection: The image (whether cartoon or real people) appears quite generic. Please consider submitting the banner with a few different photos in the middle for us to choose from. Ensure the image is a good fit and not simply a generic stock photo.

- Contact section: Kindly remove the phone number; we no longer wish to include it on the banner. Instead, please include our website (www.quellstaffing.com.au) and Instagram handle (@quellstaffing).

- Color scheme: White, black, and red/pink are preferred, or alternatively, blue. However, please avoid incorporating too many different colors as it may detract from the professional appearance.

We will be printing the design on a banner and require it to look professional and engaging.

Thank you once again for your submissions. I hope the feedback provided above is helpful.

Warm regards,

Target Market(s)

Allied Health Australia

Font styles to use
Serif

Colors
0054AA
0677BA
7BADD7
CADEEF
E8F1F8
0094D4
00A9DD
6FCCEA
C7EBF8
E9F6FB
EB3D1F
EC4F4E
F09395
F8D3D4
FCEDEE

```html
<!DOCTYPE html>
<html lang="en">
<head>
<meta charset="utf-8">
<title>Quell Staffing – Pull Up Banner</title>
<link rel="stylesheet" href="https://fonts.googleapis.com/css2?family=Montserrat:wght@400;600;700;800&display=swap">
<style>
  :root {
    --page-bg: #d2d2d2;
    --ink: #000000;
    --paper: #ffffff;
    --brand-blue: #0054aa;
    --brand-blue-dark: #003f82;
    --photo-top: #5b6468;
    --photo-mid: #8a9aab;
    --photo-low: #a79f96;
  }
  * { box-sizing: border-box; margin: 0; padding: 0; }
  html, body {
    width: 1200px; height: 1138px; overflow: hidden;
    background: var(--page-bg);
    font-family: "Montserrat", sans-serif;
  }
  .banner {
    position: absolute; left: 370px; top: 29px;
    width: 460px; height: 1080px;
    background: var(--ink);
    overflow: hidden;
  }
  .brand-tab {
    position: absolute; left: 41px; top: 0; width: 378px; height: 115px;
    background: var(--paper);
    border-radius: 0 0 28px 28px;
    display: flex; align-items: center; justify-content: center;
  }
  .brand-name {
    font-weight: 800; font-size: 31px; letter-spacing: 3px;
    color: var(--ink);
  }
  .headline {
    position: absolute; left: 0; width: 100%; top: 150px;
    text-align: center; color: var(--paper); font-weight: 700;
  }
  .headline-main { display: block; font-size: 49px; line-height: 50px; letter-spacing: -0.5px; }
  .headline-sub { display: block; font-size: 26px; line-height: 30px; }
  .hero-photo {
    position: absolute; left: 0; top: 246px; width: 100%; height: 392px;
    background: linear-gradient(180deg, var(--photo-top) 0%, var(--photo-mid) 45%, #41619a 70%, var(--photo-low) 100%);
  }
  .intro {
    position: absolute; left: 0; top: 638px; width: 100%; height: 100px;
    background: var(--paper);
    padding-top: 40px;
    text-align: center; font-weight: 600; font-size: 16px; line-height: 23px;
    color: var(--ink);
  }
  .tagline-box {
    position: absolute; left: 58px; top: 572px; width: 335px; height: 84px;
    z-index: 2;
    background: var(--brand-blue);
    color: var(--paper); text-align: center; font-weight: 700;
    padding-top: 13px;
  }
  .tagline-main { display: block; font-size: 40px; line-height: 40px; letter-spacing: 0.5px; }
  .tagline-sub { display: block; font-size: 20px; line-height: 22px; }
  .specialties {
    position: absolute; left: 58px; top: 760px; list-style: none;
    color: var(--paper); font-size: 22px; font-weight: 400; letter-spacing: 0.5px;
  }
  .specialties li { height: 31.5px; line-height: 31.5px; }
  .specialties li::before {
    content: ""; display: inline-block; width: 7px; height: 7px;
    background: var(--paper); border-radius: 50%;
    margin-right: 16px; vertical-align: middle; position: relative; top: -2px;
  }
  .contact-panel {
    position: absolute; left: 0; top: 892px; width: 100%; height: 163px;
    background: var(--paper);
  }
  .cta-tab { position: absolute; left: 110px; top: 877px; width: 240px; height: 48px; }
  .cta-label {
    position: absolute; left: 122px; top: 877px; width: 215px; height: 48px;
    color: var(--paper); font-weight: 700; font-size: 24px; letter-spacing: 0.5px;
    display: flex; align-items: center; justify-content: center;
  }
  .contact-list {
    position: absolute; left: 52px; top: 955px; list-style: none;
    font-weight: 700; font-size: 17px; color: var(--ink);
  }
  .contact-list li { height: 30px; display: flex; align-items: center; }
  .contact-icon { width: 12px; height: 12px; margin-right: 17px; flex: none; }
  .footer-band {
    position: absolute; left: 0; top: 1055px; width: 100%; height: 25px;
    background: var(--ink);
  }
</style>
</head>
<body>
  <main class="banner">
    <header class="brand-tab">
      <span class="brand-name">QUELL STAFFING</span>
    </header>

    <h1 class="headline">
      <span class="headline-main">HEALTHCARE</span>
      <span class="headline-sub">RECRUITMENT AGENCY</span>
    </h1>

    <div class="hero-photo" role="img" aria-label="Photo of five smiling medical professionals in white coats and blue scrubs with stethoscopes, standing in front of a hospital entrance"></div>

    <p class="intro">DISCOVER TAILORED OPPORTUNITIES<br>BASED ON YOUR CAREER PREFERENCES</p>

    <div class="tagline-box">
      <span class="tagline-main">EMPOWERING</span>
      <span class="tagline-sub">YOUR NEXT CAREER MOVE</span>
    </div>

    <ul class="specialties">
      <li>ALLIED HEALTH</li>
      <li>NURSING</li>
      <li>MEDICAL IMAGING</li>
    </ul>

    <section class="contact-panel" aria-label="Contact"></section>

    <svg class="cta-tab" viewBox="0 0 240 48" aria-hidden="true">
      <path d="M0 12 Q0 0 12 0 L12 12 Z" fill="var(--brand-blue-dark)"/>
      <path d="M240 12 Q240 0 228 0 L228 12 Z" fill="var(--brand-blue-dark)"/>
      <path d="M12 0 H228 V34 Q228 48 214 48 H26 Q12 48 12 34 Z" fill="var(--brand-blue)"/>
    </svg>
    <div class="cta-label">GET IN TOUCH</div>

    <ul class="contact-list">
      <li>
        <svg class="contact-icon" viewBox="0 0 12 12" aria-hidden="true">
          <g fill="none" stroke="var(--brand-blue)" stroke-width="1">
            <circle cx="6" cy="6" r="5"/>
            <ellipse cx="6" cy="6" rx="2.2" ry="5"/>
            <line x1="1" y1="6" x2="11" y2="6"/>
          </g>
        </svg>
        www.quellstaffing.com.au
      </li>
      <li>
        <svg class="contact-icon" viewBox="0 0 12 12" aria-hidden="true">
          <circle cx="6" cy="6" r="5" fill="none" stroke="var(--brand-blue)" stroke-width="1.4"/>
        </svg>
        @quellstaffing
      </li>
    </ul>

    <div class="footer-band"></div>
  </main>
</body>
</html>
```